Business card design needed

partition walls
suspended ceilings
bulkheads
shops
office fitouts
compressed sheeting

main colour aqua blue with silver and white writing

k.r.m plastering (vic) pty.ltd

noel carrow
M:0400712864 E:krmplastering@mailvane.com
ABN: 64 203 917 482
ACN: 271 604 815

```html
<!DOCTYPE html>
<html lang="en">
<head>
<meta charset="utf-8">
<title>K.R.M Plastering business card</title>
<link rel="stylesheet" href="https://fonts.googleapis.com/css2?family=Nunito:wght@800;900&family=Quicksand:wght@500&display=swap">
<style>
  :root {
    --page: #2b2f36;
    --card-top: #3d72bf;
    --card-bottom: #1f4f9a;
    --text-white: #e9eef6;
    --rule: #d7dde6;
  }
  * { margin: 0; padding: 0; box-sizing: border-box; }
  html, body { width: 1200px; height: 900px; overflow: hidden; }
  body {
    background: var(--page);
    display: flex;
    align-items: center;
    justify-content: center;
  }
  .card {
    position: relative;
    width: 900px;
    height: 520px;
    border-radius: 26px;
    background: linear-gradient(160deg, var(--card-top), var(--card-bottom));
    box-shadow: 0 20px 40px rgba(0,0,0,0.45);
    overflow: hidden;
    color: var(--text-white);
  }
  .company-name {
    position: absolute;
    left: 0;
    right: 0;
    top: 70px;
    text-align: center;
    font-family: "Quicksand", sans-serif;
    font-weight: 500;
    font-size: 30px;
    color: var(--text-white);
    white-space: nowrap;
  }
  .person-name {
    position: absolute;
    left: 250px;
    top: 195px;
    width: 240px;
    text-align: center;
    font-family: "Nunito", sans-serif;
    font-weight: 900;
    font-size: 20px;
    letter-spacing: 1.5px;
    text-transform: uppercase;
  }
  .contact, .registration {
    position: absolute;
    font-family: "Quicksand", sans-serif;
    font-weight: 500;
    font-size: 19px;
    line-height: 34px;
    white-space: nowrap;
  }
  .contact { left: 72px; top: 270px; }
  .registration { left: 590px; top: 182px; }
  .rule-v {
    position: absolute;
    width: 2px;
    background: var(--rule);
  }
  .rule-v.contact-rule { left: 55px; top: 272px; height: 66px; }
  .rule-v.reg-rule { left: 565px; top: 186px; height: 76px; }
  .rule-h {
    position: absolute;
    height: 2px;
    background: var(--rule);
  }
  .rule-h.reg-line { left: 565px; right: 0; top: 262px; }
  .rule-h.services-top { left: 0; right: 0; top: 352px; }
  .rule-h.services-bottom { left: 0; right: 0; top: 462px; }
  .services {
    position: absolute;
    left: 0;
    right: 0;
    top: 364px;
    text-align: center;
    font-family: "Nunito", sans-serif;
    font-weight: 800;
    font-size: 24px;
    line-height: 40px;
    color: var(--text-white);
  }
</style>
</head>
<body>
  <div class="card">
    <div class="company-name">K.R.M Plastering (VIC) Pty.Ltd</div>

    <div class="person-name">Noel Carrow</div>

    <div class="rule-v reg-rule"></div>
    <div class="registration">
      <div>ABN: 64 203 917 482</div>
      <div>ACN: 271 604 815</div>
    </div>
    <div class="rule-h reg-line"></div>

    <div class="rule-v contact-rule"></div>
    <div class="contact">
      <div>M:0400712864</div>
      <div>E:krmplastering@mailvane.com</div>
    </div>

    <div class="rule-h services-top"></div>
    <div class="services">
      <div>partition walls &nbsp;-&nbsp; suspended ceilings &nbsp;-&nbsp; bulkheads &nbsp;-&nbsp; shops</div>
      <div>office fitouts &nbsp;-&nbsp; compressed sheeting</div>
    </div>
    <div class="rule-h services-bottom"></div>
  </div>
</body>
</html>
```